Website incl. html for real estate project

We need the design and implementation of a website for a real estate project. Condominiums are built, which are sold.
We upload the sales brochure. The website should be based on the design of the sales brochure.
There are three houses with 5 apartments each. It should be rendered like this. The structure of the menu should be roughly as follows. Most information about the content is either in the appendix as a picture or in the brochure (PDF)):
Home (page 4-5 from the brochure)
House A
house B
house c
overview
basement
Municipal elections (page 6-7 in the brochure pdf)
Contact
Please use Roboto Regular as font.
And one page should give an overview of all apartments with the prices, the living space, etc. as on the file overview2.jpg.
If you go to the House A, House B, or House C menus, a page should come up with the details for that house only. The pages in the brochure are:
House A (Page 10-11)
House B (page 22-23)
House C (page 34-35)
The individual apartments should each be shown on a property page. There the plan / floor plan of the apartment and the pictures from the inside should be shown. As with the object page.jpg attachment.
Für die Designer... Mehr Zeit...
Coded - Design and coding required
1 page

```html
<!DOCTYPE html>
<html lang="de">
<head>
<meta charset="utf-8">
<title>Flat Detail Page</title>
<link href="https://fonts.googleapis.com/css2?family=Roboto:wght@300;400;500&family=Mulish:wght@400&family=Cormorant+Garamond:wght@500&display=swap" rel="stylesheet">
<style>
:root{
  --board:#ebebeb;
  --page:#ffffff;
  --panel:#f3f3f3;
  --ink:#1e1e1e;
  --ink-soft:#555555;
  --line:#9a9a9a;
  --line-light:#d6d6d6;
  --button:#4b4646;
  --photo-a:#d9d4cd;
  --photo-b:#8a5a48;
  --plan-a:#cfcfcf;
  --plan-b:#e8e2d9;
}
*{box-sizing:border-box;margin:0;padding:0}
html,body{width:1200px;height:3054px;overflow:hidden}
body{background:var(--board);font-family:"Roboto",sans-serif;color:var(--ink);position:relative}
.board-title{position:absolute;top:122px;left:0;width:1200px;text-align:center;font-family:"Mulish",sans-serif;font-size:66px;color:#333;letter-spacing:0.5px}
.page{position:absolute;left:95px;top:237px;width:1010px;height:2763px;background:var(--page)}
.sidebar-line{position:absolute;left:108px;top:0;width:1px;height:543px;background:var(--line)}
.brand{position:absolute;left:53px;top:124px;transform:translate(-50%,-50%) rotate(-90deg);font-family:"Cormorant Garamond",serif;font-size:19px;letter-spacing:3px;white-space:nowrap;color:#333}
.side-contact{position:absolute;left:53px;top:352px;transform:translate(-50%,-50%) rotate(-90deg);font-size:7.5px;line-height:10px;white-space:nowrap;color:#333}
.menu-btn{position:absolute;left:29px;top:456px;width:48px;height:48px;border:1px solid var(--line-light);border-radius:50%}
.menu-btn span{position:absolute;top:15px;width:1px;height:18px;background:#999}
.flat-title{position:absolute;left:108px;top:42px;width:850px;text-align:center;font-size:27px;line-height:34px;font-weight:500}
.gallery{position:absolute;left:108px;top:160px;width:902px;height:354px;background:linear-gradient(90deg,var(--photo-b) 0%,var(--photo-a) 25%,#ece9e4 55%,#cfcac3 100%)}
.gallery-arrow{position:absolute;width:40px;height:40px;border-radius:50%;background:#fff}
.features{position:absolute;left:307px;top:556px;display:grid;grid-template-columns:repeat(4,85px);column-gap:25px;row-gap:15px}
.feature{width:85px;height:99px;border:1px solid var(--line);display:flex;flex-direction:column;align-items:center;justify-content:flex-end;padding-bottom:12px;text-align:center}
.feature svg{margin-bottom:6px}
.feature .value{font-size:14px;line-height:15px}
.feature .label{font-size:9.5px;color:var(--ink-soft);line-height:11px}
.feature.price{justify-content:center;padding:0;font-size:14px;line-height:17px}
.section-title{position:absolute;left:108px;width:902px;text-align:center;font-size:28px;font-weight:400}
.floorplan-section{position:absolute;left:108px;top:849px;width:902px;height:762px;background:var(--panel)}
.floorplan-text{position:absolute;left:111px;top:107px;width:620px;text-align:center;font-size:10.5px;line-height:21.8px;white-space:nowrap}
.floorplan{position:absolute;left:161px;top:329px;width:530px;height:349px;background:linear-gradient(90deg,var(--plan-a) 0%,#eaeaea 40%,var(--plan-b) 75%,#dcdcdc 100%);border:4px solid #555}
.listing{position:absolute;left:171px;width:696px}
.listing-thumb{position:absolute;left:8px;width:140px;height:90px;background:linear-gradient(90deg,#cfcfcf,#e9e4dc 60%,#d8d8d8)}
.listing-name{position:absolute;left:185px;font-size:14px;line-height:20px}
.listing-area{position:absolute;left:185px;font-size:12px;color:var(--ink-soft)}
.listing-meta{position:absolute;font-size:12px;color:var(--ink-soft)}
.listing-go{position:absolute;left:667px;width:36px;height:36px;border-radius:50%;background:var(--button)}
.divider{position:absolute;left:171px;width:696px;height:1px;background:var(--line-light)}
.contact-section{position:absolute;left:108px;top:2260px;width:902px;height:503px;background:var(--panel)}
.field{position:absolute;top:97px;width:271px;height:38px;border:1px solid var(--line);background:#fff;font-size:11px;color:var(--ink-soft);padding:12px 0 0 25px}
.consent{position:absolute;top:173px;left:0;width:902px;text-align:center;font-size:10px}
.consent i{display:inline-block;width:9px;height:9px;background:#ccc;vertical-align:-1px;margin-right:4px}
.send{position:absolute;left:366px;top:209px;width:104px;height:29px;border-radius:15px;background:var(--button);color:#fff;font-size:11px;text-align:center;line-height:29px}
.contact-lines{position:absolute;left:0;width:902px;text-align:center}
.contact-big{font-size:24px;line-height:29px}
.contact-small{font-size:14px;line-height:20px}
.social{position:absolute;width:18px;height:18px;border-radius:50%;background:var(--ink)}
</style>
</head>
<body>
<div class="board-title">Flat Detail Page</div>

<main class="page">
  <aside>
    <div class="sidebar-line"></div>
    <div class="brand">HALDENRAIN</div>
    <div class="side-contact">+41 61 555 01 20<br>kontakt@haldenrain-wohnen.ch</div>
    <div class="menu-btn"><span style="left:19px"></span><span style="left:23px"></span><span style="left:27px"></span></div>
  </aside>

  <h1 class="flat-title">3 1/5 Zimmer Wohnung<br>Obergeschoss, Haus A</h1>

  <div class="gallery" role="img" aria-label="Innenansicht: Wohn- und Essbereich mit offener Küche">
    <div class="gallery-arrow" style="left:58px;top:157px">
      <svg width="40" height="40" viewBox="0 0 40 40"><path d="M27 20H13M19 14l-6 6 6 6" fill="none" stroke="#222" stroke-width="1.6"/></svg>
    </div>
    <div class="gallery-arrow" style="left:774px;top:164px">
      <svg width="40" height="40" viewBox="0 0 40 40"><path d="M13 20h14M21 14l6 6-6 6" fill="none" stroke="#222" stroke-width="1.6"/></svg>
    </div>
  </div>

  <div class="features">
    <div class="feature"><svg width="34" height="30" viewBox="0 0 34 30" fill="none" stroke="#444" stroke-width="1.2"><rect x="2" y="2" width="30" height="26"/><path d="M2 14h12V2M20 28V16h12"/></svg><div class="value">81 m²</div><div class="label">Wohnfläche</div></div>
    <div class="feature"><svg width="32" height="30" viewBox="0 0 32 30" fill="none" stroke="#444" stroke-width="1.2"><path d="M4 26V14h24v12M6 14V6h8v8M4 20h24"/></svg><div class="value">3,5</div><div class="label">Zimmer</div></div>
    <div class="feature"><svg width="32" height="30" viewBox="0 0 32 30" fill="none" stroke="#444" stroke-width="1.2"><path d="M4 14h24M4 28h24M8 14v14M13 14v14M19 14v14M24 14v14M10 14V3h12v11"/></svg><div class="value">16 m²</div><div class="label">Balkon</div></div>
    <div class="feature"><svg width="32" height="30" viewBox="0 0 32 30" fill="none" stroke="#444" stroke-width="1.2"><path d="M3 15h26v4a7 7 0 0 1-7 7H10a7 7 0 0 1-7-7zM7 15V5a3 3 0 0 1 6 0M9 26l-2 3M23 26l2 3"/></svg><div class="value">2</div><div class="label">Badezimmer</div></div>
    <div class="feature"><svg width="32" height="26" viewBox="0 0 32 26" fill="none" stroke="#444" stroke-width="1.2"><path d="M3 22V12h26v10M5 12V4h22v8M9 12V8h6v4M17 12V8h6v4M3 18h26"/></svg><div class="value">2</div><div class="label">Schlafzimmer</div></div>
    <div class="feature"><svg width="32" height="30" viewBox="0 0 32 30" fill="none" stroke="#444" stroke-width="1.2"><path d="M3 28h26M3 28V20h6v-6h6V8h6V2h8v26M20 28V18h6v10"/></svg><div class="value">11 m²</div><div class="label">Kelleraum</div></div>
    <div class="feature"><svg width="30" height="30" viewBox="0 0 30 30" fill="none" stroke="#444" stroke-width="1.2"><circle cx="15" cy="5" r="3"/><path d="M5 10l10 3 10-3M15 13v8M15 21l-5 8M15 21l5 8"/></svg><div class="value">100%</div><div class="label">Barrierefrei</div></div>
    <div class="feature price">CHF<br>640’000</div>
  </div>

  <section class="floorplan-section">
    <h2 class="section-title" style="left:0;top:33px">Grundriss</h2>
    <p class="floorplan-text">Der kompakt, durchdachte Grundriss und die hellen Räume beinhalten<br>diverse Extras. Ein praktisches Reduit, die moderne Küche mit Kochinsel, der grosszügige Wohn- und<br>Essbereich gehören neben dem über 33 Quadratmeter grossen Balkon zu den Highlights dieser Wohnung.<br>Die beiden Badezimmer sind jeweils mit einer Dusche ausgestattet. Eines der Badezimmer ist direkt durch das<br>angrenzende Elternschlafzimmer „en Suite“ zugänglich und neben der Dusche mit einer Badewanne<br>ausgestattet. Der Wäscheturm mit Waschmaschine/Tumbler ist im Reduit integriert. Wer das perfekte<br>Zuhause für eine Familie oder Paare sucht ist bei dieser Wohnung genau richtig</p>
    <div class="floorplan" role="img" aria-label="Möblierter Grundriss der 3 1/5 Zimmer Wohnung mit Balkon, Küche, Wohnbereich, zwei Bädern und zwei Schlafzimmern"></div>
  </section>

  <section>
    <h2 class="section-title" style="top:1680px;left:168px;width:800px">Weitere Wohnungen</h2>

    <div class="listing" style="top:1764px">
      <div class="listing-thumb" style="top:0" role="img" aria-label="Grundriss Erdgeschoss, Haus A"></div>
      <div class="listing-name" style="top:17px">3 1/5 Zimmer Wohnung<br>Erdgeschoss, Haus A</div>
      <div class="listing-area" style="top:65px">102 m² Wohnfläche</div>
      <div class="listing-meta" style="left:391px;top:20px">3 Schlafzimmer</div>
      <div class="listing-meta" style="left:508px;top:20px">2 Badezimmer</div>
      <div class="listing-go" style="top:14px"><svg width="36" height="36" viewBox="0 0 36 36"><path d="M16 12l6 6-6 6" fill="none" stroke="#fff" stroke-width="1.5"/></svg></div>
    </div>
    <div class="divider" style="top:1871px"></div>

    <div class="listing" style="top:1894px">
      <div class="listing-thumb" style="top:0" role="img" aria-label="Grundriss Obergeschoss, Haus A"></div>
      <div class="listing-name" style="top:17px;left:183px">4,5Zimmer Wohnung<br>Obergeschoss, Haus A</div>
      <div class="listing-area" style="top:60px;left:183px">102 m² Wohnfläche</div>
      <div class="listing-meta" style="left:389px;top:20px">2 Schlafzimmer</div>
      <div class="listing-meta" style="left:506px;top:20px">2 Badezimmer</div>
      <div class="listing-go" style="top:10px"><svg width="36" height="36" viewBox="0 0 36 36"><path d="M16 12l6 6-6 6" fill="none" stroke="#fff" stroke-width="1.5"/></svg></div>
    </div>
    <div class="divider" style="top:2007px"></div>

    <div class="listing" style="top:2031px">
      <div class="listing-thumb" style="top:0" role="img" aria-label="Grundriss Erdgeschoss, Haus A"></div>
      <div class="listing-name" style="top:17px">4,5 Zimmer Wohnung<br>Erdgeschoss, Haus A</div>
      <div class="listing-area" style="top:65px">102 m² Wohnfläche</div>
      <div class="listing-meta" style="left:391px;top:20px">3 Schlafzimmer</div>
      <div class="listing-meta" style="left:508px;top:20px">2 Badezimmer</div>
      <div class="listing-go" style="top:15px"><svg width="36" height="36" viewBox="0 0 36 36"><path d="M16 12l6 6-6 6" fill="none" stroke="#fff" stroke-width="1.5"/></svg></div>
    </div>
  </section>

  <section class="contact-section">
    <h2 class="section-title" style="left:0;top:44px;font-size:27px">Kontakt</h2>
    <div class="field" style="left:149px">Name*</div>
    <div class="field" style="left:443px">Email*</div>
    <div class="consent"><i></i>I accept The Terms for processing personal data.</div>
    <div class="send">Send Request</div>
    <div class="contact-lines" style="top:291px">
      <div class="contact-big">+41 61 555 01 20</div>
      <div class="contact-big">kontakt@haldenrain-wohnen.ch</div>
    </div>
    <div class="contact-lines contact-small" style="top:360px">Lena Hofer, Lindenweg 12,<br>4410 Liestal</div>
    <div class="social" style="left:379px;top:433px"></div>
    <div class="social" style="left:411px;top:433px"></div>
    <div class="social" style="left:443px;top:433px"></div>
  </section>
</main>
</body>
</html>
```